Redesign and move to Wordpress for quarvendo.com

Our website needs a redesign and at the same time we are moving it to Wordpress. Please help us with a new digital professional look and feel.

We are an Australian Software Engineering company specialising in advanced software development using in A.I., PLatform Engineering, Integration and Cloud. See the current quarvendo.com for more information about us.

```html
<!DOCTYPE html>
<html lang="en">
<head>
<meta charset="utf-8">
<title>quarvendo — Reliable Smart Software Engineering</title>
<link href="https://fonts.googleapis.com/css2?family=Krona+One&family=Barlow:wght@300;400;500;600&display=swap" rel="stylesheet">
<style>
:root{
  --night:#0b0a1a;
  --night-2:#14132a;
  --teal:#52c5bd;
  --blue:#1d5fa3;
  --white:#ffffff;
  --muted:#9a9aa8;
  --ink:#1b1b1b;
  --line:#cfeeed;
}
*{box-sizing:border-box;margin:0;padding:0}
html,body{width:1200px;height:3138px;overflow:hidden}
body{background:var(--night);font-family:"Barlow",sans-serif;color:var(--white);position:relative}
.abs{position:absolute}
.display{font-family:"Krona One",sans-serif;font-weight:400}

/* hero */
.hero{position:absolute;left:0;top:0;width:1200px;height:625px;
  background:radial-gradient(ellipse at 50% 40%,#1a2a3a 0%,#101528 45%,#0b0a1a 100%)}
.hero-pattern{position:absolute;inset:0;background:linear-gradient(120deg,rgba(82,197,189,.06),rgba(29,95,163,.05) 50%,rgba(82,197,189,.04))}
.brand{position:absolute;display:flex;align-items:center;gap:10px;font-weight:500;color:var(--white)}
.brand-mark{width:30px;height:30px;border:2px solid var(--white)}
.nav{position:absolute;top:17px;left:100px;width:1000px;height:36px}
.nav .brand{left:0;top:0;font-size:28px;letter-spacing:1px}
.nav-links{position:absolute;left:517px;top:9px;display:flex;gap:36px;font-size:15px}
.search{position:absolute;left:830px;top:0;width:170px;height:34px;border-radius:6px;background:rgba(255,255,255,.08);
  font-size:15px;color:#b5b5c0;padding:8px 12px}
.search svg{position:absolute;right:10px;top:8px}
.hero h1{position:absolute;left:0;width:1200px;top:197px;text-align:center;font-size:37px;line-height:40px;color:var(--teal)}
.hero p{position:absolute;left:260px;width:680px;top:324px;text-align:center;font-size:14.5px;line-height:21.5px;color:#d6d6de}
.btn-teal{position:absolute;background:var(--teal);color:var(--white);font-weight:500;text-align:center;border-radius:3px}
.hero .btn-teal{left:515px;top:419px;width:170px;height:33px;line-height:33px;font-size:14px}
.hero-bar{position:absolute;left:100px;top:546px;width:1000px;height:55px;border-radius:10px;background:rgba(255,255,255,.07)}

/* services */
.services{position:absolute;left:0;top:625px;width:1200px;height:717px;background:var(--white);color:var(--ink)}
.section-title{position:absolute;left:0;width:1200px;text-align:center;font-size:36px}
.services .section-title{top:53px;color:var(--blue)}
.service{position:absolute;left:100px;width:1000px;height:80px}
.service-icon{position:absolute;left:0;top:8px;width:50px;height:50px;border-radius:8px;background:linear-gradient(135deg,#1d5fa3,#3a86c8)}
.service h3{position:absolute;left:92px;top:0;width:200px;font-size:19px;line-height:22px;font-weight:600;color:var(--blue)}
.service p{position:absolute;left:330px;top:-4px;width:475px;font-size:10.5px;line-height:15.7px;color:var(--ink)}
.divider{position:absolute;left:100px;width:1000px;height:2px;background:linear-gradient(90deg,var(--line),#eaf7f6 80%,transparent)}
.btn-blue{position:absolute;left:100px;top:589px;width:133px;height:34px;line-height:34px;text-align:center;background:var(--blue);
  color:var(--white);font-weight:500;font-size:14px;border-radius:3px}

/* news */
.news{position:absolute;left:0;top:1342px;width:1200px;height:524px;background:var(--night)}
.news .section-title{top:112px;color:var(--teal)}
.card{position:absolute;top:202px;width:233px;height:176px;border:1px solid #3b3b52;border-radius:10px;background:var(--night-2);padding:22px 15px}
.card h4{font-size:13.5px;font-weight:600;margin-bottom:24px}
.card p{font-size:10px;line-height:15.6px;color:#d8d8e0;height:64px}
.card p u{text-decoration:underline}
.card a{display:block;margin-top:6px;font-size:10px;color:var(--teal);text-decoration:none}

/* cta */
.cta{position:absolute;left:0;top:1866px;width:1200px;height:214px;background:var(--teal)}
.cta h2{position:absolute;left:100px;top:48px;width:520px;font-size:30px;line-height:38px;color:var(--white)}
.subscribe{position:absolute;left:704px;top:84px;width:286px;height:47px;background:var(--night);border-radius:4px}
.subscribe .field{position:absolute;left:14px;top:16px;font-size:10px;color:var(--teal);display:flex;gap:6px;align-items:center}
.subscribe .go{position:absolute;right:12px;top:12px;width:58px;height:22px;background:var(--white);color:var(--night);font-size:10px;text-align:center;line-height:22px;border-radius:3px}

/* appointment */
.appt{position:absolute;left:0;top:2080px;width:1200px;height:640px}
.appt .kicker{position:absolute;left:100px;top:69px;font-size:25px;font-weight:300}
.appt h2{position:absolute;left:100px;top:100px;font-size:24px}
.appt .lede{position:absolute;left:100px;top:146px;font-size:10.5px}
.input{position:absolute;height:26px;border:1px solid #7ad8d1;border-radius:2px;font-size:9.5px;color:#c8c8d0;padding:7px 8px}
.slot-label{position:absolute;left:108px;top:2403px;font-size:9.5px}
.slot{position:absolute;left:108px;font-size:9.5px;display:flex;align-items:center;gap:10px}
.radio{width:14px;height:14px;border:1.5px solid var(--teal);border-radius:50%;position:relative}
.radio.on::after{content:"";position:absolute;left:2px;top:2px;width:7px;height:7px;border-radius:50%;background:var(--teal)}
.appt-art{position:absolute;left:629px;top:2248px;width:466px;height:399px;border-radius:6px;
  background:linear-gradient(180deg,var(--teal) 0 24px,#f4f4f7 24px 270px,var(--night) 270px)}

/* footer */
.footer .brand{left:100px;top:2781px;font-size:34px;gap:14px}
.footer .brand .brand-mark{width:48px;height:48px}
.about-text{position:absolute;left:100px;top:2853px;width:260px;font-size:14px;line-height:20px;color:#c9c9d2}
.about-text span{color:var(--teal)}
.follow{position:absolute;left:100px;top:2976px;font-size:10px;color:var(--teal)}
.socials{position:absolute;left:100px;top:2998px;display:flex;gap:12px}
.socials i{display:block;width:16px;height:16px;border-radius:50%;background:var(--teal)}
.col{position:absolute;top:2782px}
.col h5{font-size:17px;font-weight:600;color:var(--teal);margin-bottom:22px}
.col li{list-style:none;font-size:14px;color:#8a8a98;margin-bottom:17px}
.contact{position:absolute;left:932px;display:flex;gap:14px}
.contact small{display:block;font-size:11px;color:#9a9aa8}
.contact b{display:block;font-size:13.5px;font-weight:400;color:var(--teal);margin-top:4px}
.rule{position:absolute;left:107px;top:3044px;width:986px;height:1px;background:#55556a}
.legal{position:absolute;left:107px;top:3068px;display:flex;gap:34px;font-size:11px;color:#8a8a98}
.copy{position:absolute;right:107px;top:3068px;font-size:11px;color:#8a8a98}
</style>
</head>
<body>

<header class="hero">
  <div class="hero-pattern" role="img" aria-label="Faint pattern of overlapping outlined squares"></div>
  <nav class="nav">
    <div class="brand"><span class="brand-mark"></span>quarvendo</div>
    <div class="nav-links"><span>Services</span><span>Contact</span><span>About</span><span>Blog</span></div>
    <div class="search">Search
      <svg width="20" height="20" viewBox="0 0 20 20" fill="none" stroke="#fff" stroke-width="2"><circle cx="8.5" cy="8.5" r="6.5"/><line x1="13.5" y1="13.5" x2="18.5" y2="18.5"/></svg>
    </div>
  </nav>
  <h1 class="display">Reliable Smart<br>Software Engineeting</h1>
  <p>At Quarvendo, we craft bespoke software solutions that are not available on the market. By building organizations market-leading products, process automation, legacy system enablement, or advanced intelligent systems, we empower our customers to achieve a competitive edge in their industry.</p>
  <div class="btn-teal">Explore Now</div>
  <div class="hero-bar"></div>
</header>

<section class="services">
  <h2 class="section-title display">Our Services</h2>
  <div class="service" style="top:165px">
    <div class="service-icon" role="img" aria-label="Icon of a monitor with a gear"></div>
    <h3>Enterprise Systems Integration</h3>
    <p>Enterprise systems integration is the process of connecting various IT systems, applications, and data sources within an organization to work seamlessly together. This integration enables the smooth flow of information across different departments and functions, enhancing overall efficiency and productivity.</p>
  </div>
  <div class="divider" style="top:270px"></div>
  <div class="service" style="top:313px">
    <div class="service-icon" role="img" aria-label="Icon of connected documents"></div>
    <h3>Platform engineering</h3>
    <p>Enterprise systems integration is the process of connecting various IT systems, applications, and data sources within an organization to work seamlessly together. This integration enables the smooth flow of information across different departments and functions, enhancing overall efficiency and productivity.</p>
  </div>
  <div class="divider" style="top:418px"></div>
  <div class="service" style="top:473px">
    <div class="service-icon" role="img" aria-label="Icon of a cloud with a gear and nodes"></div>
    <h3>Real-time DATA stream PROCESSING</h3>
    <p>Enterprise systems integration is the process of connecting various IT systems, applications, and data sources within an organization to work seamlessly together. This integration enables the smooth flow of information across different departments and functions, enhancing overall efficiency and productivity.</p>
  </div>
  <div class="btn-blue">Learn More</div>
</section>

<section class="news">
  <h2 class="section-title display">News &amp; Articles</h2>
  <article class="card" style="left:101px">
    <h4>AI in SOFTWARE ENGINEERING</h4>
    <p>10 unexpected ways to use CodeWing Assist (CodeWing Journal) CodeWing Assist is widely known for its code generation feature.</p>
    <a>Read More</a>
  </article>
  <article class="card" style="left:357px">
    <h4>Business Insights</h4>
    <p>How Storytelling Helps Data-driven Teams Succeed (Halvern School of Management) Winning leaders know that data alone isn't enough.</p>
    <a>Read More</a>
  </article>
  <article class="card" style="left:612px">
    <h4>INDUSTRY RESEARCH</h4>
    <p><u>PROMTA: A general-purpose framework for prompt optimization</u> (Northlake Research) Large language models (LLMs) have revolutionized various tasks,</p>
    <a>Read More</a>
  </article>
  <article class="card" style="left:868px">
    <h4>Artificial intelligence</h4>
    <p>(Northlake Research) Northlake discusses Prompting strategies that demonstrates how the generalist Orin-4 model can perform as a specialist on</p>
    <a>Read More</a>
  </article>
</section>

<section class="cta">
  <h2 class="display">Book an obligation free consultation with our Lead Technologist</h2>
  <div class="subscribe">
    <div class="field">
      <svg width="13" height="10" viewBox="0 0 13 10" fill="none" stroke="#52c5bd"><rect x=".5" y=".5" width="12" height="9" rx="1"/><path d="M1 1l5.5 4L12 1"/></svg>
      Enter your email
    </div>
    <div class="go">Submit</div>
  </div>
</section>

<section class="appt">
  <div class="kicker">Make An</div>
  <h2 class="display">Book Appointment</h2>
  <div class="lede">Schedule Your Obligation-Free Consultation with Our Expert Technologists</div>
</section>
<div class="input" style="left:100px;top:2272px;width:137px">First Name</div>
<div class="input" style="left:250px;top:2272px;width:137px">Last Name</div>
<div class="input" style="left:100px;top:2313px;width:287px">Email Id</div>
<div class="input" style="left:100px;top:2354px;width:287px">Phone No.</div>
<div class="slot-label">Select Available Slot</div>
<div class="slot" style="top:2424px"><span class="radio on"></span>20 Jan 2025,&nbsp; 12 : 00 PM : 01 : 30</div>
<div class="slot" style="top:2452px"><span class="radio"></span>20 Jan 2025,&nbsp; 12 : 00 PM : 01 : 30</div>
<div class="slot" style="top:2479px"><span class="radio"></span>20 Jan 2025,&nbsp; 12 : 00 PM : 01 : 30</div>
<div class="input" style="left:100px;top:2514px;width:287px;height:80px">Message</div>
<div class="btn-teal" style="left:100px;top:2613px;width:287px;height:33px;line-height:33px;font-size:14px;color:var(--night);font-weight:600">Submit</div>
<div class="appt-art" role="img" aria-label="Illustration of a person pointing at a booking calendar"></div>

<footer class="footer">
  <div class="brand"><span class="brand-mark"></span>quarvendo</div>
  <p class="about-text">We ara a lorem ipsum dolor sit amet, consectetur adipiscing elit, sed do eiusmod tempor incididunt ut labore exercitation ullamco laboris nisi ut aliquip ex ea commodo consequat... <span>Read More</span></p>
  <div class="follow">Follow Us</div>
  <div class="socials" aria-label="Social links"><i></i><i></i><i></i></div>

  <div class="col" style="left:470px"><h5>Support</h5><ul><li>Contact Us</li><li>Online Chat</li><li>Whisperly</li><li>Wiregram</li><li>Ticketing</li></ul></div>
  <div class="col" style="left:616px"><h5>About</h5><ul><li>About Us</li><li>Contact</li><li>About</li><li>Blog</li></ul></div>
  <div class="col" style="left:761px"><h5>FAQ</h5><ul><li>Account</li><li>Manage Deliveries</li><li>Orders</li><li>Payments</li><li>Returns</li></ul></div>

  <div class="contact" style="top:2784px">
    <svg width="22" height="22" viewBox="0 0 24 24" fill="none" stroke="#c9c9d2" stroke-width="1.6"><path d="M5 3h4l2 5-3 2a11 11 0 0 0 6 6l2-3 5 2v4a2 2 0 0 1-2 2A17 17 0 0 1 3 5a2 2 0 0 1 2-2z"/></svg>
    <div><small>Tel</small><b>100 - 200 - 30...</b></div>
  </div>
  <div class="contact" style="top:2847px">
    <svg width="22" height="22" viewBox="0 0 24 24" fill="none" stroke="#c9c9d2" stroke-width="1.6"><rect x="2" y="5" width="20" height="14" rx="1"/><path d="M2 6l10 7 10-7"/></svg>
    <div><small>Mail</small><b>hello@quarvendo.com</b></div>
  </div>
  <div class="contact" style="top:2910px">
    <svg width="22" height="22" viewBox="0 0 24 24" fill="none" stroke="#c9c9d2" stroke-width="1.6"><path d="M12 22s7-7 7-12a7 7 0 0 0-14 0c0 5 7 12 7 12z"/><circle cx="12" cy="10" r="2.5"/></svg>
    <div><small>Address</small><b style="margin-top:12px">Harbour City, AU</b></div>
  </div>

  <div class="rule"></div>
  <div class="legal"><span>About us</span><span>Contact</span><span>Privacy policy</span><span>Sitemap</span><span>Terms of Use</span></div>
  <div class="copy">© 2025, All Rights Reserved</div>
</footer>

</body>
</html>
```